Luxury Skincare Product Box Packaging Design

Vorastelle is a range of skincare products that help protect, nourish, and strengthen even the most sensitive skin, ensuring it is healthy, glowing, calm, and soft. Skincare practices support skin to enhance its appearance and relieve skin conditions. Your skin reflects your health. It is your body canvas and is an asset. The products contain naturally derived ingredients, aromatherapy oils, sustainable and ethical ingredients, organic ingredients where possible, natural preservatives and Australian oils, fruits, and extracts.

Vorastelle
Tagline is "Where Calm Finds Bloom"

Our products do not contain sulphates, parabens, phthalates, petrochemicals, synthetic colours, nor synthetic fragrances.

Everything about the Vorastelle Skincare name is creative and communicates luxury. Vorastelle from your first glance of the name, you will know that this is a company with excellent products.

By keeping it simple, unique, and elegant is often associated with high quality and is a way to establish trust. Vorastelle is a product that is “pure” and natural, so Vorastelle packaging would look simple, elegant, and clean.

I have uploaded the actual logo design and individual labels for the current skincare range I currently with the ingredients included so you can get an understanding of what I like. I have also added samples of package designs I quite like to assist with your designs.

Each Product box packaging sizes are as follows:

Product One - Exfoliating Herbs: 110mm (H) x 33mm Diameter
Product Two - Probiotic Lotion: 138mm (H) x 33mm Diameter
Product Three - Vitamin A Serum: 120mm (H) x 30mm Diameter
Updates

The Measurements are as follows: Product One: 110mm (H) x 33mm Diameter Product Two: 138mm (H) x 33mm Diameter Product Three: 120mm (H) x 30mm Diameter

Target Market(s)

Women

Requirements
Must have
• Logo, Product Name and ingredients and if you can barcode on the packaging that is the box design I am after
Nice to have
• samples of designs I like but open to suggestions

```html
<!DOCTYPE html>
<html lang="en">
<head>
<meta charset="utf-8">
<title>Vorastelle – Gentle Exfoliating Herbs Box</title>
<link href="https://fonts.googleapis.com/css2?family=Lato:wght@300;400&display=swap" rel="stylesheet">
<style>
  :root {
    --backdrop: #d8ece1;
    --panel-white: #ffffff;
    --rose-dark: #8e6150;
    --rose-mid: #c99179;
    --rose-light: #f6c8ad;
    --rose-text: #b47c64;
    --ink: #1c1c1c;
    --leaf: #4f8a45;
    --leaf-deep: #2f5f2c;
    --petal: #f7f7f2;
  }
  html, body {
    margin: 0;
    padding: 0;
    width: 1200px;
    height: 800px;
    overflow: hidden;
    background: var(--backdrop);
    font-family: "Lato", sans-serif;
  }
  .canvas {
    position: relative;
    width: 1200px;
    height: 800px;
  }
  .box-front {
    position: absolute;
    left: 150px;
    top: 230px;
    width: 900px;
    height: 340px;
    display: flex;
    background: var(--panel-white);
    box-shadow: 0 18px 40px rgba(60, 90, 75, 0.12);
  }
  .side-band {
    width: 66px;
    background: linear-gradient(90deg, var(--rose-dark), var(--rose-mid) 55%, var(--rose-light));
  }
  .side-band--right {
    position: relative;
    width: 120px;
    background: linear-gradient(180deg, var(--rose-light), var(--rose-mid) 60%, var(--rose-dark));
  }
  .product-name {
    position: absolute;
    left: 50%;
    bottom: 96px;
    transform: translateX(-50%) rotate(180deg);
    writing-mode: vertical-rl;
    white-space: nowrap;
    color: var(--panel-white);
    font-weight: 400;
    font-size: 17px;
    letter-spacing: 0.06em;
    line-height: 1.35;
  }
  .product-name span {
    display: block;
  }
  .face {
    position: relative;
    flex: 1;
  }
  .botanical {
    position: absolute;
    left: 0;
    top: 0;
    width: 200px;
    height: 170px;
    border-radius: 0 0 70% 0;
    background:
      radial-gradient(ellipse at 45% 38%, var(--petal) 0 30%, rgba(247, 247, 242, 0) 46%),
      linear-gradient(135deg, var(--leaf-deep), var(--leaf) 60%, rgba(79, 138, 69, 0.6));
  }
  .wordmark {
    position: absolute;
    left: 300px;
    top: 118px;
    width: 400px;
    text-align: center;
  }
  .brand {
    margin: 0;
    color: var(--rose-text);
    font-weight: 300;
    font-size: 76px;
    letter-spacing: 0.02em;
    line-height: 1;
  }
  .tagline {
    margin: 16px 0 0;
    color: var(--ink);
    font-weight: 400;
    font-size: 15px;
    letter-spacing: 0.22em;
  }
</style>
</head>
<body>
<main class="canvas">
  <section class="box-front">
    <div class="side-band"></div>
    <div class="face">
      <div class="botanical" role="img" aria-label="White jasmine blossom with green leaves"></div>
      <div class="wordmark">
        <h1 class="brand">Vorastelle</h1>
        <p class="tagline">Where Calm Finds Bloom</p>
      </div>
    </div>
    <div class="side-band side-band--right">
      <div class="product-name"><span>Gentle</span><span>Exfoliating Herbs</span></div>
    </div>
  </section>
</main>
</body>
</html>
```